Business Card Design

I need a business card for my resume writing business. I have a logo that Im not keen on anymore so I would like the business card to use my photo instead of a logo. I am for mid career and trades resumes and prefer not to do executive resumes so don't need to aim for exectives. I would like it to be colourful. I like bright sky blue and maybe some pink or purple but primarily bright sky blue. I don't like green and Im keen see a fair bit of white on the card. As I have a photo to go it, it will need to go on a white background.

Target Market(s)

mid range careers. Not executives

Industry/Entity Type

Business

Contact Information for Business Card

Lise Varncombe
Resume Writer
Bright Path CVs
27 The Gullwing
HALDORN NSW 2391
lise@brightpathcvs.com.au
0417263958
www.brightpathcvs.com.au

Requirements
Nice to have
• Maybe colours similar to my website - www.brightpathcvs.com.au but not with any black on it.
Should not have
• No green or dark colours

```html
<!DOCTYPE html>
<html lang="en">
<head>
<meta charset="utf-8">
<title>Bright Path CVs – Business Card</title>
<link rel="stylesheet" href="https://fonts.googleapis.com/css2?family=Ubuntu:wght@500&family=Open+Sans:wght@400&display=swap">
<style>
  :root {
    --sky: #2ba3e0;
    --sky-deep: #1a86c4;
    --sky-light: #35b0ea;
    --ink: #2b2b2b;
    --ink-soft: #3c3c3c;
    --rule: #555;
    --paper: #ffffff;
    --paper-shade: #f1f1f1;
    --photo-warm: #e6e1dc;
    --photo-cool: #efefef;
    --stage: #e9ecef;
  }
  * { box-sizing: border-box; margin: 0; padding: 0; }
  html, body {
    width: 1200px; height: 1024px; overflow: hidden;
    background: var(--stage);
  }
  .canvas { position: relative; width: 1200px; height: 1024px; }
  .card {
    position: absolute; left: 200px; width: 800px; height: 457px;
    border-radius: 4px; overflow: hidden;
    box-shadow: 0 6px 18px rgba(0,0,0,.12);
  }
  .card--front {
    top: 40px;
    background: linear-gradient(90deg, var(--paper-shade) 0%, var(--paper) 45%);
  }
  .brand {
    position: absolute; left: 48px; top: 44px;
    font-family: "Ubuntu", sans-serif; font-weight: 500;
    font-size: 44px; letter-spacing: 1px; color: var(--sky);
    text-transform: uppercase; white-space: nowrap; line-height: 1.2;
  }
  .name-row {
    position: absolute; left: 78px; top: 190px; width: 360px;
    display: flex; align-items: flex-end; gap: 6px;
  }
  .name {
    font-family: "Open Sans", sans-serif; font-size: 30px;
    color: var(--ink); white-space: nowrap; line-height: 1;
  }
  .name-rule { flex: 1; height: 1px; background: var(--rule); margin-bottom: 4px; }
  .contacts {
    position: absolute; left: 78px; top: 250px; list-style: none;
    font-family: "Open Sans", sans-serif; font-size: 17px; color: var(--ink-soft);
  }
  .contacts li { display: flex; align-items: center; gap: 14px; height: 36px; white-space: nowrap; }
  .contacts svg { width: 20px; height: 20px; flex: none; }
  .portrait {
    position: absolute; right: 0; top: 0; width: 340px; height: 457px;
    background: linear-gradient(90deg, rgba(255,255,255,0) 0%, var(--photo-cool) 25%, var(--photo-warm) 100%);
  }
  .card--back {
    top: 527px;
    background: radial-gradient(ellipse 70% 80% at 55% 45%, var(--sky-light) 0%, var(--sky) 50%, var(--sky-deep) 100%);
    display: flex; align-items: center; justify-content: center;
  }
  .brand--reverse {
    position: static; color: var(--paper); font-size: 56px; letter-spacing: 2px;
  }
</style>
</head>
<body>
<main class="canvas">
  <section class="card card--front">
    <div class="portrait" role="img" aria-label="Portrait photo of Lise Varncombe"></div>
    <h1 class="brand">Bright Path CVs</h1>
    <div class="name-row">
      <span class="name">Lise Varncombe</span>
      <span class="name-rule"></span>
    </div>
    <ul class="contacts">
      <li>
        <svg viewBox="0 0 20 20" aria-hidden="true"><path d="M5 2c1 0 2 3 2 4s-2 1-1 3 2 4 4 5 2-1 3-1 4 1 4 2-2 3-3 3C8 18 2 12 2 5c0-1 2-3 3-3z" fill="var(--sky)"/></svg>
        0417263958
      </li>
      <li>
        <svg viewBox="0 0 20 20" aria-hidden="true"><rect x="2" y="5" width="16" height="11" rx="1.5" fill="var(--sky)"/><path d="M2.5 6l7.5 6 7.5-6" stroke="#fff" stroke-width="1.5" fill="none"/></svg>
        lise@brightpathcvs.com.au
      </li>
      <li>
        <svg viewBox="0 0 20 20" aria-hidden="true"><circle cx="10" cy="10" r="8" fill="var(--sky)"/><g stroke="#fff" stroke-width="1.1" fill="none"><ellipse cx="10" cy="10" rx="3.5" ry="8"/><path d="M2 10h16M3.5 6h13M3.5 14h13"/></g></svg>
        www.brightpathcvs.com.au
      </li>
      <li>
        <svg viewBox="0 0 20 20" aria-hidden="true"><path d="M10 2a6 6 0 0 1 6 6c0 4-6 10-6 10S4 12 4 8a6 6 0 0 1 6-6z" fill="var(--sky)"/><circle cx="10" cy="8" r="2.2" fill="#fff"/></svg>
        27 The Gullwing HALDORN NSW 2391
      </li>
    </ul>
  </section>
  <section class="card card--back">
    <h2 class="brand brand--reverse">Bright Path CVs</h2>
  </section>
</main>
</body>
</html>
```